Update Financial Planning Presentation

We currently use a stock Powerpoint template. Information is imputed into an Excel spreadsheet and then linked to the presentation. We are looking to improve and upgrade this to a more straightforward and "cleaner" looking template. I have attached a sample copy of the Powerpoint presantation we currently use along with the Excel spreadsheet. I have attached our logo as well. Thanks.
Industry/Entity Type
Financial

```html
<!DOCTYPE html>
<html lang="en">
<head>
<meta charset="utf-8">
<title>Common Lifecycle Periods</title>
<link href="https://fonts.googleapis.com/css2?family=Ubuntu:wght@400;500;700&display=swap" rel="stylesheet">
<style>
  :root {
    --brand-green: #3b9633;
    --row-tint: #ccffcc;
    --panel-white: #ffffff;
    --text-body: #474747;
    --header-dark: #5a3422;
    --header-mid: #8a5a3c;
    --header-light: #b07f58;
    --rule-green: #3b9633;
    --silhouette: #1e1e1e;
  }
  * { box-sizing: border-box; margin: 0; padding: 0; }
  html, body { width: 1200px; height: 900px; overflow: hidden; background: #ffffff; }
  body { font-family: "Ubuntu", sans-serif; position: relative; }

  .slide { position: relative; width: 1200px; height: 900px; background: #ffffff; overflow: hidden; }

  .title-bar {
    position: absolute; left: 0; top: 0; width: 1200px; height: 112px;
    background: radial-gradient(ellipse at 45% 20%, var(--header-light) 0%, var(--header-mid) 35%, var(--header-dark) 100%);
    border-bottom: 3px solid var(--rule-green);
  }
  .title-bar-image { position: absolute; inset: 0; }
  .slide-title {
    position: absolute; left: 36px; top: 32px;
    font-size: 40px; font-weight: 500; color: #ffffff; letter-spacing: 1px;
    text-shadow: 1px 2px 2px rgba(0,0,0,0.45);
  }
  .brand-name {
    position: absolute; right: 16px; top: 36px;
    font-size: 40px; font-weight: 700; color: #ffffff; letter-spacing: -0.5px;
  }

  .lifecycle-table {
    position: absolute; left: 75px; top: 231px; width: 1050px; height: 462px;
    background: var(--brand-green); border-radius: 12px;
  }
  .table-head { position: absolute; left: 0; top: 0; width: 100%; height: 60px; }
  .table-head span {
    position: absolute; top: 16px; font-size: 26px; font-weight: 500;
    color: #ffffff; letter-spacing: 0.5px;
  }
  .table-body {
    position: absolute; left: 9px; top: 60px; width: 1032px; height: 393px;
    background: var(--panel-white); border-radius: 10px;
  }
  .row { position: absolute; left: 6px; width: 1020px; height: 56px; }
  .row.tinted { background: var(--row-tint); }
  .row span { position: absolute; top: 13px; font-size: 27px; color: var(--text-body); }
  .col-period { left: 37px; }
  .col-age { left: 415px; }
  .col-profile { left: 631px; }
  .head-period { left: 51px; }
  .head-age { left: 445px; }
  .head-profile { left: 649px; }

  .corner-mark {
    position: absolute; left: 22px; top: 778px; width: 60px; height: 122px;
    background: linear-gradient(180deg, #3a3a3a, var(--silhouette));
    border-radius: 30px 30px 4px 4px;
  }
  .footer-band {
    position: absolute; left: 0; top: 860px; width: 1200px; height: 40px;
    background: var(--brand-green);
  }
  .footer-note {
    position: absolute; right: 14px; top: 10px; font-size: 19px; color: #ffffff;
  }
</style>
</head>
<body>
<div class="slide">
  <header class="title-bar">
    <div class="title-bar-image" role="img" aria-label="Warm brown textured banner background"></div>
    <h1 class="slide-title">COMMON LIFECYCLE PERIODS</h1>
    <div class="brand-name">harborleaf financial</div>
  </header>

  <section class="lifecycle-table">
    <div class="table-head">
      <span class="head-period">LIFECYCLE PERIODS</span>
      <span class="head-age">AGE</span>
      <span class="head-profile">FINANCIAL PROFILE</span>
    </div>
    <div class="table-body">
      <div class="row" style="top:6px">
        <span class="col-period">Early Career</span><span class="col-age">25-40</span><span class="col-profile">Debts: Mortgage, etc.</span>
      </div>
      <div class="row tinted" style="top:81px">
        <span class="col-period">Mid-career</span><span class="col-age">40-50</span><span class="col-profile">Debt Elimination</span>
      </div>
      <div class="row" style="top:156px">
        <span class="col-period">Accumulation</span><span class="col-age">50-60</span><span class="col-profile">Peak Savings Period</span>
      </div>
      <div class="row tinted" style="top:231px">
        <span class="col-period">Pre-retirement</span><span class="col-age">60-65</span><span class="col-profile">Retirement &amp; Estate Planning</span>
      </div>
      <div class="row" style="top:306px">
        <span class="col-period">Retirement</span><span class="col-age">Age 65+</span><span class="col-profile">Health and Lifestyle Changes</span>
      </div>
    </div>
  </section>

  <div class="corner-mark" role="img" aria-label="Dark silhouette of a standing wading bird"></div>
  <footer class="footer-band">
    <span class="footer-note">Copyright text here</span>
  </footer>
</div>
</body>
</html>
```